Design Creative Banner or Gif Ads. 3 Designs To Be Selected

Come up with some creative banner ads for stonewell.co.nz

*At least 3 different winning banners will be chosen*

Please provide banner ads / gif ads in common google ads / website banner formats.

They can be gif or static but must stand out while still maintaining clear clean text and visuals, with a premium professional feel (please avoid clip art or anything that gives a cheap message).

Please keep in mind that these will likely be small ads so text needs to be large and if there's there a lot of text then use multiple frames/ pages as submit as a gif.

Style
Minimal & clean lines
Architectural or realistic images
Avoid cartoon styles, clipart, or anything that looks cheap

Font
Nexa or Montserrat or similar

Tone
Premium, serious, trustworthy — fits new builds

Colours
Option 1: Deep Navy (trust & quality) & lighter blues and warm grey
Option 2: Open to bright colours to help the ads stand out, such as (but not limited to) bright pink with black, yellow, fluorescent green, provided the messaging is still done professionally.
Our logo is attached (Stone Well Logo)

Display Sizes
Ad specs for file sizes should be file formats like JPEG, GIF, and PNG, with animations limited to a max of 30 seconds or less.
We will need several different ad sizes provided for each of the 3 selected winning designs.

• Medium Rectangle: 300 × 250 pixels
• Leaderboard: 728 × 90 pixels
• Desktop Banner ad image: (640x360 pixels)
• Desktop Banner ad image 2: (300x600 pixels)
• Possibly one or two other sizes

Flexibility to be creative
The ad text, words, upper/lower case, layout, colour, theme, and images can be adjusted to how you think it will look best. The follow example ads are just examples of what we are after but we are keen to see what you can create.

Recommendations at this point:
1. Avoid text heavy
2. Looking for more Gif ads
3. Imaging: if possible use real stock photo's rather than AI

Themes:

1
Building Soon? Start Here
Free Build Planning Pack:
✓ Build Cost Calculator
✓ Hidden Cost Checklist
✓ Builder Comparison Guide
Build With Confidence
Download Free

2
Before You Choose A Builder
Compare Price, Scope, Risk & Value
Avoid Costly Mistakes
Choose The Right Builder With Confidence
Download The Free Guide

3
Planning A New Build?
Avoid These Common Mistakes:
✗ Hidden Exclusions
✗ Missing Scope
✗ Unrealistic Allowances
✗ Budget Blowouts
Download The Free Guide

4
Before You Buy Land
Know what it could cost to build.
Avoid Costly Building Mistakes
Download Our Free Guides

5
Know Your Build Budget?
• Free Build Cost Calculator
• Hidden Cost Checklist
• Build Planning Tools
Calculate Costs (Download)

Target Market(s)

Landowners looking to build

Industry/Entity Type

Building

Font styles to use
Other font styles liked:
• Nexa or Montserrat or similar

Requirements
Should not have
• Avoid cartoon styles, clipart, or anything that looks cheap

```html
<!DOCTYPE html>
<html lang="en">
<head>
<meta charset="utf-8">
<title>Stone Well – Building Soon? Banner Set</title>
<link rel="stylesheet" href="https://fonts.googleapis.com/css2?family=Montserrat:wght@800&family=Raleway:wght@500;600;700&family=Kalam:wght@400&display=swap">
<style>
  :root{
    --navy:#0c3858;
    --navy-deep:#082c47;
    --accent-blue:#2b8cc4;
    --button-top:#3ca3d6;
    --button-bottom:#1d7bb1;
    --white:#ffffff;
    --ink:#1f2a33;
    --logo-navy:#153a57;
    --page:#ebe7e1;
    --photo-light:#eef0f2;
    --photo-mid:#d9dde1;
    --photo-warm:#c9a48a;
  }
  *{margin:0;padding:0;box-sizing:border-box;}
  html,body{width:794px;height:1200px;overflow:hidden;background:var(--page);}
  .canvas{position:relative;width:794px;height:1200px;}

  .banner{position:absolute;overflow:hidden;}
  .photo{position:absolute;inset:0;
    background:
      radial-gradient(ellipse at 72% 62%, rgba(201,164,138,.55) 0 14%, transparent 34%),
      radial-gradient(ellipse at 30% 45%, rgba(176,160,170,.45) 0 10%, transparent 26%),
      linear-gradient(135deg,var(--photo-light) 0%,var(--photo-mid) 55%,#f4f5f6 100%);}
  .shapes{position:absolute;inset:0;width:100%;height:100%;}

  .t{position:absolute;white-space:nowrap;transform:translateY(-50%);line-height:1;}
  .tc{position:absolute;white-space:nowrap;transform:translate(-50%,-50%);line-height:1;text-align:center;}

  .headline{font-family:"Montserrat",sans-serif;font-weight:800;color:var(--white);letter-spacing:-.02em;}
  .pack-title{font-family:"Raleway",sans-serif;font-weight:600;color:var(--white);}
  .benefit{font-family:"Raleway",sans-serif;font-weight:500;color:var(--white);display:flex;align-items:center;}
  .benefit.two-line{white-space:normal;line-height:1.05;}
  .tick{display:inline-block;flex:none;border:1.5px solid var(--white);border-radius:50%;position:relative;}
  .tick::after{content:"";position:absolute;left:32%;top:18%;width:28%;height:46%;
    border-right:1.5px solid var(--white);border-bottom:1.5px solid var(--white);transform:rotate(40deg);}
  .divider{position:absolute;background:linear-gradient(90deg,transparent,rgba(255,255,255,.35),transparent);height:1px;}
  .divider.vertical{width:1px;background:rgba(255,255,255,.3);}
  .cta{position:absolute;display:flex;align-items:center;justify-content:center;
    background:linear-gradient(var(--button-top),var(--button-bottom));color:var(--white);
    font-family:"Raleway",sans-serif;font-weight:600;border-radius:3px;
    box-shadow:0 2px 3px rgba(0,0,0,.25);white-space:nowrap;}
  .tagline{font-family:"Kalam",cursive;color:var(--ink);}
  .tagline.on-navy{color:var(--white);}
  .brand{font-family:"Raleway",sans-serif;font-weight:700;color:var(--logo-navy);}
</style>
</head>
<body>
<div class="canvas">

  <!-- Desktop banner 640x360 -->
  <section class="banner" style="left:82px;top:84px;width:558px;height:314px;">
    <div class="photo" role="img" aria-label="Photo of hands sketching house plans with a pen beside a small model house"></div>
    <svg class="shapes" viewBox="0 0 558 314" aria-hidden="true">
      <defs><linearGradient id="navy1" x1="0" y1="0" x2="1" y2="1"><stop offset="0" stop-color="#0e3d60"/><stop offset="1" stop-color="#082c47"/></linearGradient></defs>
      <polygon points="270,0 285,0 320,143 281,314 266,314 306,143" fill="var(--accent-blue)"/>
      <polygon points="0,0 276,0 309,143 266,314 0,314" fill="url(#navy1)"/>
    </svg>
    <div class="tc headline" style="left:143px;top:52px;font-size:39px;">BUILDING</div>
    <div class="tc headline" style="left:143px;top:95px;font-size:39px;">SOON?</div>
    <div class="tc headline" style="left:143px;top:138px;font-size:39px;">START HERE</div>
    <div class="divider" style="left:35px;top:168px;width:218px;"></div>
    <div class="t pack-title" style="left:25px;top:187px;font-size:18.5px;">Free Build Planning Pack:</div>
    <div class="t benefit" style="left:24px;top:222px;font-size:16px;"><span class="tick" style="width:14px;height:14px;margin-right:8px;"></span>Build Cost Calculator</div>
    <div class="t benefit" style="left:24px;top:245px;font-size:16px;"><span class="tick" style="width:14px;height:14px;margin-right:8px;"></span>Hidden Cost Checklist</div>
    <div class="t benefit" style="left:24px;top:268px;font-size:16px;"><span class="tick" style="width:14px;height:14px;margin-right:8px;"></span>Builder Comparison Guide</div>
    <div class="t brand" style="left:350px;top:50px;font-size:24px;">Stone Well</div>
    <div class="cta" style="left:341px;top:240px;width:171px;height:39px;font-size:17px;">Download Free &gt;</div>
    <div class="tc tagline" style="left:426px;top:294px;font-size:15px;">Build With Confidence</div>
  </section>

  <!-- Leaderboard 728x90 -->
  <section class="banner" style="left:81px;top:418px;width:408px;height:52px;">
    <div class="photo" role="img" aria-label="Photo of hands sketching house plans beside a small model house"></div>
    <svg class="shapes" viewBox="0 0 408 52" aria-hidden="true">
      <polygon points="304,0 311,0 324,26 308,52 301,52 316,26" fill="var(--accent-blue)"/>
      <polygon points="0,0 219,0 215,52 0,52" fill="var(--navy)"/>
    </svg>
    <div class="t headline" style="left:6px;top:16px;font-size:15.5px;">BUILDING SOON?</div>
    <div class="t headline" style="left:7px;top:35px;font-size:21.5px;">START HERE</div>
    <div class="divider vertical" style="left:152px;top:6px;height:40px;"></div>
    <div class="t pack-title" style="left:155px;top:15px;font-size:5.5px;">Free Build Planning Pack:</div>
    <div class="t benefit" style="left:155px;top:23px;font-size:4.6px;"><span class="tick" style="width:4px;height:4px;margin-right:2px;border-width:.6px;"></span>Build Cost Calculator</div>
    <div class="t benefit" style="left:155px;top:30px;font-size:4.6px;"><span class="tick" style="width:4px;height:4px;margin-right:2px;border-width:.6px;"></span>Hidden Cost Checklist</div>
    <div class="t benefit" style="left:155px;top:37px;font-size:4.6px;"><span class="tick" style="width:4px;height:4px;margin-right:2px;border-width:.6px;"></span>Builder Comparison Guide</div>
    <div class="t brand" style="left:238px;top:12px;font-size:8px;">Stone Well</div>
    <div class="cta" style="left:237px;top:24px;width:63px;height:15px;font-size:6.3px;border-radius:2px;">Download Free &gt;</div>
    <div class="tc tagline" style="left:268px;top:45px;font-size:5.5px;">Build With Confidence</div>
  </section>

  <!-- Wide banner -->
  <section class="banner" style="left:79px;top:489px;width:634px;height:78px;">
    <div class="photo" role="img" aria-label="Photo of hands sketching house plans beside a small model house"></div>
    <svg class="shapes" viewBox="0 0 634 78" aria-hidden="true">
      <polygon points="468,0 477,0 498,39 477,78 468,78 489,39" fill="var(--accent-blue)"/>
      <polygon points="336,0 345,0 364,39 345,78 336,78 355,39" fill="var(--accent-blue)"/>
      <polygon points="0,0 340,0 357,39 340,78 0,78" fill="var(--navy)"/>
    </svg>
    <div class="t headline" style="left:9px;top:24px;font-size:24px;">BUILDING SOON?</div>
    <div class="t headline" style="left:11px;top:53px;font-size:33px;">START HERE</div>
    <div class="divider vertical" style="left:236px;top:9px;height:60px;"></div>
    <div class="t pack-title" style="left:243px;top:23px;font-size:8.5px;">Free Build Planning Pack:</div>
    <div class="t benefit" style="left:243px;top:36px;font-size:7.4px;"><span class="tick" style="width:6px;height:6px;margin-right:3px;border-width:.8px;"></span>Build Cost Calculator</div>
    <div class="t benefit" style="left:243px;top:46px;font-size:7.4px;"><span class="tick" style="width:6px;height:6px;margin-right:3px;border-width:.8px;"></span>Hidden Cost Checklist</div>
    <div class="t benefit" style="left:243px;top:56px;font-size:7.4px;"><span class="tick" style="width:6px;height:6px;margin-right:3px;border-width:.8px;"></span>Builder Comparison Guide</div>
    <div class="t brand" style="left:374px;top:19px;font-size:12px;">Stone Well</div>
    <div class="cta" style="left:369px;top:37px;width:97px;height:21px;font-size:9.5px;border-radius:2px;">Download Free &gt;</div>
    <div class="tc tagline" style="left:418px;top:66px;font-size:8px;">Build With Confidence</div>
  </section>

  <!-- Half page 300x600 -->
  <section class="banner" style="left:83px;top:588px;width:261px;height:523px;">
    <div class="photo" role="img" aria-label="Photo of hands sketching house plans beside a small model house"></div>
    <svg class="shapes" viewBox="0 0 261 523" aria-hidden="true">
      <defs><linearGradient id="navy4" x1="0" y1="0" x2="0" y2="1"><stop offset="0" stop-color="#0a304e"/><stop offset="1" stop-color="#0e3d60"/></linearGradient></defs>
      <polygon points="0,203 135,169 261,203 261,215 135,181 0,215" fill="var(--accent-blue)"/>
      <polygon points="0,214 135,180 261,214 261,523 0,523" fill="url(#navy4)"/>
    </svg>
    <div class="t brand" style="left:60px;top:35px;font-size:21px;">Stone Well</div>
    <div class="tc headline" style="left:132px;top:237px;font-size:35px;">BUILDING</div>
    <div class="tc headline" style="left:132px;top:275px;font-size:35px;">SOON?</div>
    <div class="tc headline" style="left:132px;top:314px;font-size:35px;">START HERE</div>
    <div class="divider" style="left:20px;top:340px;width:222px;"></div>
    <div class="tc pack-title" style="left:132px;top:357px;font-size:16.5px;">Free Build Planning Pack:</div>
    <div class="t benefit" style="left:27px;top:388px;font-size:15px;"><span class="tick" style="width:13px;height:13px;margin-right:7px;"></span>Build Cost Calculator</div>
    <div class="t benefit" style="left:27px;top:409px;font-size:15px;"><span class="tick" style="width:13px;height:13px;margin-right:7px;"></span>Hidden Cost Checklist</div>
    <div class="t benefit" style="left:27px;top:430px;font-size:15px;"><span class="tick" style="width:13px;height:13px;margin-right:7px;"></span>Builder Comparison Guide</div>
    <div class="cta" style="left:44px;top:454px;width:173px;height:40px;font-size:17px;">Download Free &gt;</div>
    <div class="tc tagline on-navy" style="left:130px;top:506px;font-size:12px;">Build With Confidence</div>
  </section>

  <!-- Medium rectangle 300x250 -->
  <section class="banner" style="left:389px;top:590px;width:262px;height:217px;">
    <div class="photo" role="img" aria-label="Photo of hands sketching house plans with a pen"></div>
    <svg class="shapes" viewBox="0 0 262 217" aria-hidden="true">
      <polygon points="103,0 113,0 146,108 113,217 103,217 136,108" fill="var(--accent-blue)"/>
      <polygon points="0,0 109,0 140,108 107,217 0,217" fill="var(--navy)"/>
    </svg>
    <div class="t headline" style="left:9px;top:23px;font-size:17.5px;">BUILDING</div>
    <div class="t headline" style="left:9px;top:41px;font-size:17.5px;">SOON?</div>
    <div class="t headline" style="left:9px;top:60px;font-size:17.5px;">START HERE</div>
    <div class="divider" style="left:9px;top:73px;width:110px;"></div>
    <div class="t pack-title" style="left:9px;top:84px;font-size:9.5px;">Free Build Planning Pack:</div>
    <div class="t benefit two-line" style="left:9px;top:106px;font-size:9.5px;width:110px;"><span class="tick" style="width:14px;height:14px;margin-right:6px;"></span>Build Cost<br>Calculator</div>
    <div class="t benefit two-line" style="left:9px;top:129px;font-size:9.5px;width:110px;"><span class="tick" style="width:14px;height:14px;margin-right:6px;"></span>Hidden Cost<br>Checklist</div>
    <div class="t benefit two-line" style="left:9px;top:152px;font-size:9.5px;width:110px;"><span class="tick" style="width:14px;height:14px;margin-right:6px;"></span>Builder<br>Comparison Guide</div>
    <div class="cta" style="left:10px;top:174px;width:94px;height:21px;font-size:9.5px;border-radius:2px;">Download Free &gt;</div>
    <div class="tc tagline on-navy" style="left:56px;top:204px;font-size:8px;">Build With Confidence</div>
    <div class="t brand" style="left:167px;top:193px;font-size:13px;">Stone Well</div>
  </section>

  <!-- Rectangle -->
  <section class="banner" style="left:388px;top:827px;width:293px;height:243px;">
    <div class="photo" role="img" aria-label="Photo of hands sketching house plans with a pen"></div>
    <svg class="shapes" viewBox="0 0 293 243" aria-hidden="true">
      <polygon points="114,0 125,0 162,118 125,243 114,243 151,118" fill="var(--accent-blue)"/>
      <polygon points="0,0 120,0 156,118 120,243 0,243" fill="var(--navy)"/>
    </svg>
    <div class="t headline" style="left:10px;top:26px;font-size:19.5px;">BUILDING</div>
    <div class="t headline" style="left:10px;top:46px;font-size:19.5px;">SOON?</div>
    <div class="t headline" style="left:10px;top:67px;font-size:19.5px;">START HERE</div>
    <div class="t pack-title" style="left:10px;top:93px;font-size:10.5px;">Free Build Planning Pack:</div>
    <div class="t benefit two-line" style="left:11px;top:119px;font-size:10.5px;width:130px;"><span class="tick" style="width:16px;height:16px;margin-right:7px;"></span>Build Cost<br>Calculator</div>
    <div class="t benefit two-line" style="left:11px;top:145px;font-size:10.5px;width:130px;"><span class="tick" style="width:16px;height:16px;margin-right:7px;"></span>Hidden Cost<br>Checklist</div>
    <div class="t benefit two-line" style="left:11px;top:171px;font-size:10.5px;width:130px;"><span class="tick" style="width:16px;height:16px;margin-right:7px;"></span>Builder<br>Comparison Guide</div>
    <div class="cta" style="left:11px;top:194px;width:106px;height:24px;font-size:10.5px;border-radius:2px;">Download Free &gt;</div>
    <div class="tc tagline on-navy" style="left:63px;top:229px;font-size:9px;">Build With Confidence</div>
    <div class="t brand" style="left:188px;top:215px;font-size:15px;">Stone Well</div>
  </section>

</div>
</body>
</html>
```